Energy trading company (Voltrisa) needs a business card

We need a business card for a company based in Central America. Our main purpose is trading energy . We already have the logo but we need some good creativity to design a high impact business card. Colors blue, orange, green can be used or we would like to see good combinatios with our logo

Target Market(s)

Energy

Industry/Entity Type

Power Generation

Contact Information for Business Card

Logo , headquarters , name, background

Font styles to use
Serif
Sans Serif

Colors

Designer to choose colors to be used in the design.

Requirements
Must have
• it must have a fresh and clean view
Nice to have
• good backgrounds that combine with the logo
Should not have
• too much words

```html
<!DOCTYPE html>
<html lang="en">
<head>
<meta charset="utf-8">
<title>Voltrisa Business Card</title>
<link rel="stylesheet" href="https://fonts.googleapis.com/css2?family=Lato:wght@400;700&display=swap">
<style>
  :root {
    --backdrop: #2a2b2d;
    --card: #0b0c0c;
    --silver: #8c8d90;
    --silver-light: #a7a8ab;
    --text-muted: #7d7e81;
    --rule: #2e3031;
    --accent: #f0801f;
  }
  * { margin: 0; padding: 0; box-sizing: border-box; }
  html, body {
    width: 1200px; height: 970px; overflow: hidden;
    background: var(--backdrop);
    font-family: "Lato", sans-serif;
  }
  .canvas {
    position: relative; width: 1200px; height: 970px;
    display: flex; flex-direction: column; align-items: center; justify-content: center; gap: 50px;
  }
  .card {
    position: relative; width: 700px; height: 400px;
    background: var(--card);
    border-bottom: 7px solid var(--accent);
    box-shadow: 0 10px 30px rgba(0,0,0,.45);
    overflow: hidden;
  }
  .brand { display: flex; flex-direction: column; align-items: center; color: var(--silver); }
  .brand-dot {
    border-radius: 50%; background: var(--silver);
  }
  .brand-name { font-weight: 400; letter-spacing: .04em; text-transform: uppercase; line-height: 1; }

  /* front */
  .card-front .brand { position: absolute; left: 50px; top: 125px; width: 270px; }
  .card-front .brand-dot { width: 64px; height: 64px; margin-bottom: 16px; }
  .card-front .brand-name { font-size: 46px; }
  .divider {
    position: absolute; left: 350px; top: 95px; width: 1px; height: 210px; background: var(--rule);
  }
  .details { position: absolute; left: 385px; top: 95px; color: var(--text-muted); }
  .person-name { font-size: 26px; font-weight: 700; color: var(--silver-light); letter-spacing: .02em; }
  .person-role { font-size: 17px; margin-top: 2px; }
  .address { font-size: 16px; line-height: 1.2; margin-top: 16px; }
  .contacts { list-style: none; margin-top: 14px; font-size: 16px; }
  .contacts li { display: flex; align-items: center; gap: 12px; height: 26px; }
  .contacts svg { width: 16px; height: 16px; fill: none; stroke: var(--text-muted); stroke-width: 1.6; }

  /* back */
  .card-back .brand { position: absolute; inset: 0; justify-content: center; }
  .card-back .brand-dot { width: 84px; height: 84px; margin-bottom: 20px; }
  .card-back .brand-name { font-size: 64px; }
</style>
</head>
<body>
<main class="canvas">
  <section class="card card-front">
    <div class="brand">
      <span class="brand-dot"></span>
      <span class="brand-name">Voltrisa</span>
    </div>
    <div class="divider"></div>
    <div class="details">
      <p class="person-name">JOHN SMITH</p>
      <p class="person-role">Position</p>
      <p class="address">2345 First Address Line<br>Second Address Line, 56324</p>
      <ul class="contacts">
        <li>
          <svg viewBox="0 0 16 16"><path d="M4 1.5l2.2 3-1.4 1.6c.8 1.9 2.2 3.4 4.1 4.2l1.6-1.4 3 2.2-1.3 2.6C6.9 13.5 2.5 9.1 1.4 3.8z"/></svg>
          <span>123 456 7890</span>
        </li>
        <li>
          <svg viewBox="0 0 16 16"><rect x="1.5" y="3.5" width="13" height="9"/><path d="M1.5 3.5L8 9l6.5-5.5"/></svg>
          <span>lorem@yourwebsite.com</span>
        </li>
        <li>
          <svg viewBox="0 0 16 16"><circle cx="8" cy="8" r="6.5"/><path d="M1.5 8h13M8 1.5c-3 3.5-3 9.5 0 13M8 1.5c3 3.5 3 9.5 0 13"/></svg>
          <span>www.yourwebsite.com</span>
        </li>
      </ul>
    </div>
  </section>

  <section class="card card-back">
    <div class="brand">
      <span class="brand-dot"></span>
      <span class="brand-name">Voltrisa</span>
    </div>
  </section>
</main>
</body>
</html>
```